"Breathe & Bloom" Book Cover 5.5x8.5

Title of the book is "Breathe & Bloom"
Subtitle is "Unmasking Pricing Myths"
I've used PixelGuild on multiple occasions you can look on my Borvex page, Mark Delwitt, to see the covers I've used in the other projects I've done.
The target audience are people who have been tricked to think they can't retire because inflation, i.e. cost of living is going up so much they must work to keep up. There is no evidence of this.
And those are the people I want to reach so they can "Breathe...and Bloom."
Target Market(s)
Americans aged 55 and over who are thinking about retirement
Industry/Entity Type
Financial
Requirements
Nice to have
- Keep It Simple, Stupid is my mantra. Just make it pop out when people are browsing
Should not have
- No piggy banks. No old people sitting on a beach.

```html
<!DOCTYPE html>
<html lang="en">
<head>
<meta charset="utf-8">
<title>Breathe &amp; Bloom – Book Cover</title>
<link href="https://fonts.googleapis.com/css2?family=Cinzel:wght@400;500&display=swap" rel="stylesheet">
<style>
  :root {
    --stage: #dfe7ef;
    --cover-blue: #5487b7;
    --sky-top: #6f9ccf;
    --sky-light: #a9c6e6;
    --cloud-blue: #9fb6d2;
    --cloud-white: #eef1f6;
    --cloud-grey: #c7d0dd;
    --type-white: #ffffff;
    --type-shadow: rgba(20, 45, 80, 0.35);
  }
  * { margin: 0; padding: 0; box-sizing: border-box; }
  html, body {
    width: 1200px;
    height: 848px;
    overflow: hidden;
    background: var(--stage);
  }
  .book-cover {
    position: absolute;
    left: 335px;
    top: 0;
    width: 530px;
    height: 848px;
    background: var(--cover-blue);
    overflow: hidden;
    font-family: "Cinzel", "Trajan Pro", serif;
    color: var(--type-white);
  }
  .sky-strip {
    position: absolute;
    left: 0;
    top: 0;
    width: 100%;
    height: 90px;
    background: linear-gradient(180deg, var(--sky-top) 0%, #80a9d8 55%, var(--sky-light) 100%);
  }
  .cloud-bank {
    position: absolute;
    left: 0;
    top: 506px;
    width: 100%;
    height: 180px;
    background: linear-gradient(180deg, var(--cloud-blue) 0%, var(--cloud-white) 35%, var(--cloud-grey) 60%, var(--cloud-white) 80%, #d9dee6 100%);
  }
  .title-line,
  .title-amp,
  .subtitle,
  .author {
    position: absolute;
    left: 0;
    width: 100%;
    text-align: center;
    white-space: nowrap;
    text-shadow: 3px 4px 8px var(--type-shadow);
  }
  .title-line {
    font-weight: 500;
    line-height: 1;
  }
  .title-top {
    top: 142px;
    font-size: 90px;
  }
  .title-amp {
    top: 243px;
    font-size: 48px;
    line-height: 1;
    font-weight: 500;
  }
  .title-bottom {
    top: 296px;
    font-size: 112px;
    letter-spacing: 2px;
  }
  .subtitle {
    top: 436px;
    font-size: 22px;
    letter-spacing: 3.5px;
    line-height: 1;
  }
  .author {
    top: 752px;
    font-size: 42px;
    letter-spacing: 6px;
    line-height: 1;
  }
</style>
</head>
<body>
  <main class="book-cover">
    <div class="sky-strip" role="img" aria-label="Photograph of a blue sky with thin wispy clouds"></div>

    <h1 class="book-title">
      <span class="title-line title-top">Breathe</span>
      <span class="title-amp">&amp;</span>
      <span class="title-line title-bottom">Bloom</span>
    </h1>
    <p class="subtitle">Unmasking Pricing Myths</p>

    <div class="cloud-bank" role="img" aria-label="Photograph of a soft bank of white clouds seen from above"></div>

    <p class="author">Mark Delwitt</p>
  </main>
</body>
</html>
```